Flyer für Vertrieb und Montage von Photovoltaikanlagen
Zielgruppe
Vertrieb und Montage von Photovoltaikanlagen für jeden Hausbesitzer
Aufgabenstellung
auf unsere WEB Site kann der Kunde sich vorab die Gesamtkosten der Anlage ausrechnen
ohne Angabe seine Identität preiszugeben

```html
<!DOCTYPE html>
<html lang="de">
<head>
<meta charset="utf-8">
<title>Birkenhain Solar – Flyer</title>
<link href="https://fonts.googleapis.com/css2?family=Open+Sans:wght@400;600;700;800&display=swap" rel="stylesheet">
<style>
  :root {
    --bg: #e4e5e7;
    --paper: #f6f6f6;
    --blue: #1d5ea8;
    --blue-dark: #164a86;
    --ink: #2b2f36;
    --muted: #6b7077;
    --white: #ffffff;
  }
  * { margin: 0; padding: 0; box-sizing: border-box; }
  html, body {
    width: 1200px; height: 1200px; overflow: hidden;
    background: var(--bg);
    font-family: "Open Sans", Arial, sans-serif;
  }
  .canvas { position: relative; width: 1200px; height: 1200px; }
  .flyer {
    position: absolute; top: 174px;
    width: 434px; height: 870px;
    background: var(--paper);
    overflow: hidden;
  }
  .flyer--front { left: 128px; }
  .flyer--back { left: 651px; }

  .brand {
    position: absolute; left: 0; right: 0;
    display: flex; align-items: center; justify-content: center; gap: 10px;
    color: var(--blue);
    font-weight: 800; letter-spacing: 0.5px;
  }
  .brand__dot { width: 22px; height: 22px; border-radius: 50%; background: var(--blue); }
  .flyer--front .brand { top: 88px; font-size: 30px; }
  .flyer--back .brand { top: 690px; font-size: 22px; }
  .flyer--back .brand__dot { width: 16px; height: 16px; }

  .photo { position: absolute; left: 0; right: 0; }
  .photo--roof {
    top: 212px; height: 453px;
    background: linear-gradient(180deg, #a9cbe8 0%, #c8d6e2 28%, #8e9297 55%, #7a7c80 100%);
  }
  .photo--install {
    top: 0; height: 155px;
    background: linear-gradient(160deg, #c9d8ea 0%, #3d5f95 45%, #223e74 100%);
  }

  .headline-band {
    position: absolute; left: 39px; right: 0; top: 557px; height: 108px;
    background: rgba(29, 94, 168, 0.9);
    display: flex; align-items: center; justify-content: flex-end;
    padding-right: 48px;
  }
  .headline-band__text {
    color: var(--white); font-weight: 800; font-size: 15.5px;
    letter-spacing: 1.2px; text-transform: uppercase; text-align: right; line-height: 1.3;
  }
  .headline-band__rule {
    position: absolute; right: 24px; top: 40px; bottom: 0; width: 4px; background: var(--white);
  }

  .calc-cta {
    position: absolute; right: 27px; top: 692px;
    display: flex; align-items: center; gap: 16px;
  }
  .calc-cta__text {
    text-align: right; color: var(--ink); font-weight: 700; font-size: 18.5px; line-height: 1.25;
  }

  .contact {
    position: absolute; font-size: 10.6px; line-height: 1.68; color: var(--muted);
  }
  .flyer--front .contact { right: 27px; top: 790px; text-align: right; }
  .flyer--back .contact { left: 0; right: 0; top: 788px; text-align: center; }

  .intro { position: absolute; left: 58px; right: 40px; top: 186px; }
  .intro__title { color: var(--blue); font-size: 22.5px; font-weight: 700; line-height: 1.25; }
  .intro__text { margin-top: 6px; color: var(--muted); font-size: 14px; line-height: 1.4; }

  .benefits { position: absolute; left: 58px; right: 30px; top: 332px; list-style: none; }
  .benefit { display: flex; gap: 18px; height: 106px; }
  .benefit__icon { flex: none; width: 42px; height: 42px; margin-top: 8px; }
  .benefit__title { color: var(--ink); font-size: 15px; font-weight: 700; margin-bottom: 6px; }
  .benefit__text { color: var(--muted); font-size: 12px; line-height: 1.55; }
</style>
</head>
<body>
<main class="canvas">

  <section class="flyer flyer--front">
    <div class="brand"><span class="brand__dot"></span>Birkenhain Solar</div>

    <div class="photo photo--roof" role="img" aria-label="Foto: Ziegeldach mit Solarmodulen, Schornstein und Dachfenstern vor blauem Himmel"></div>

    <div class="headline-band">
      <p class="headline-band__text">Senken Sie Ihre Stromkosten<br>mit einer Photovoltaikanlage</p>
      <span class="headline-band__rule"></span>
    </div>

    <div class="calc-cta">
      <p class="calc-cta__text">Berechnen Sie jetzt<br>Ihre Gesamtkosten online!</p>
      <svg width="44" height="44" viewBox="0 0 44 44" aria-hidden="true">
        <rect x="1.5" y="1.5" width="41" height="41" rx="2" fill="none" stroke="var(--blue)" stroke-width="3"/>
        <rect x="9" y="8" width="26" height="11" fill="var(--blue)"/>
        <rect x="9" y="25" width="6" height="4" fill="var(--blue)"/>
        <rect x="19" y="25" width="6" height="4" fill="var(--blue)"/>
        <rect x="29" y="25" width="6" height="11" fill="var(--blue)"/>
        <rect x="9" y="32" width="6" height="4" fill="var(--blue)"/>
        <rect x="19" y="32" width="6" height="4" fill="var(--blue)"/>
      </svg>
    </div>

    <address class="contact" style="font-style:normal">
      Address: Alder Lane 14, Hexton HX4 2PL, United Kingdom<br>
      E-mail: kontakt@birkenhain-solar.de &nbsp;|&nbsp; Web: www.birkenhain-solar.de<br>
      Phone: +44 1632 960410 &nbsp;|&nbsp; +44 1632 960420
    </address>
  </section>

  <section class="flyer flyer--back">
    <div class="photo photo--install" role="img" aria-label="Foto: Monteur befestigt Solarmodule auf einem Dach"></div>

    <div class="intro">
      <h2 class="intro__title">Sie denken über eine Photovoltaikanlage nach?</h2>
      <p class="intro__text">Nutzen Sie unseren Online-Rechner und lassen Sie sich von den Einsparungen überzeugen!</p>
    </div>

    <ul class="benefits">
      <li class="benefit">
        <svg class="benefit__icon" viewBox="0 0 42 42" aria-hidden="true">
          <circle cx="21" cy="21" r="21" fill="var(--blue)"/>
          <path d="M13 20 L21 13 L29 20 V29 H13 Z" fill="none" stroke="var(--white)" stroke-width="1.6" stroke-linejoin="round"/>
          <circle cx="21" cy="23" r="2.5" fill="none" stroke="var(--white)" stroke-width="1.4"/>
        </svg>
        <div>
          <h3 class="benefit__title">Zuverlässigkeit</h3>
          <p class="benefit__text">Vertrauen Sie auf unsere Zuverlässigkeit -<br>von der Beratung bis zur Installation Ihrer<br>Photovoltaikanlage.</p>
        </div>
      </li>
      <li class="benefit">
        <svg class="benefit__icon" viewBox="0 0 42 42" aria-hidden="true">
          <circle cx="21" cy="21" r="21" fill="var(--blue)"/>
          <circle cx="21" cy="21" r="8" fill="none" stroke="var(--white)" stroke-width="1.6"/>
          <path d="M17 21 H25 M21 17 V25" stroke="var(--white)" stroke-width="1.6"/>
          <path d="M11 21 H13 M29 21 H31" stroke="var(--white)" stroke-width="1.6"/>
        </svg>
        <div>
          <h3 class="benefit__title">Effizienz</h3>
          <p class="benefit__text">Unsere Photovoltaikanlagen:<br>Effizient und nachhaltig für Ihren Haushalt.</p>
        </div>
      </li>
      <li class="benefit">
        <svg class="benefit__icon" viewBox="0 0 42 42" aria-hidden="true">
          <circle cx="21" cy="21" r="21" fill="var(--blue)"/>
          <circle cx="21" cy="21" r="10" fill="none" stroke="var(--white)" stroke-width="1.5"/>
          <path d="M18 15 V19 M24 15 V19 M16 19 H26 V22 A5 5 0 0 1 16 22 Z M21 27 V30" fill="none" stroke="var(--white)" stroke-width="1.5" stroke-linejoin="round"/>
        </svg>
        <div>
          <h3 class="benefit__title">Geld sparen</h3>
          <p class="benefit__text">Machen Sie sich unabhängig von<br>Strompreissteigerungen.</p>
        </div>
      </li>
    </ul>

    <div class="brand"><span class="brand__dot"></span>Birkenhain Solar</div>

    <address class="contact" style="font-style:normal">
      Address: Alder Lane 14, Hexton HX4 2PL, United Kingdom<br>
      E-mail: kontakt@birkenhain-solar.de &nbsp;|&nbsp; Web: www.birkenhain-solar.de<br>
      Phone: +44 1632 960410 &nbsp;|&nbsp; +44 1632 960420
    </address>
  </section>

</main>
</body>
</html>
```